Popup Nightclub Grand Opening Flyer

We need to design a flyer for the grand opening of an upscale, exclusive nightclub called "Lanternfall". The design needs to be chic and exclusive. The background should be black and the text should primarily be white. We like minimalist designs.

Here is the text for the flyer
-
Velvetrope Atlanta Presents

Lanternfall (LOGO)

A Popup Nightclub Experience
For one night Only

Friday, October 18, 2013
Party begins at 9PM

INVITE ONLY

See invitation for location details
(Velvetrope Atlanta logo)

-
Examples we like

http://cdn2-b.brivelpost.com/sites/default/files/styles/image_content_width/hash/3d/fa/1472093815_4471_flyer.jpg?itok=R8kqWm2z

http://api.plovra.com/files/7Kqq-Tr82XXB3pQzJvmtR5HL2W719E4nbRtC6KLd4HsfM8Y2qTDK-VmjwDoNqLX4QBzTHD9nakRbVx3m-Pfq8htc3MDTWr5p4/2zelSaturdays.jpg

http://quenmar.com/wp-content/uploads/yootheme/widgetkit/gallery/2zel/2zel-gen_vroom4-01.jpg

Hi All, one thing that we are seeing that we don't like is on over emphasis on the phrase "a popup nightclub experience" please don't make this the largest thing on the flyer

Target Market(s)

Target market is 25-35 year olds who are affluent (rich) and like luxury brands

Requirements
Must have
• Dark Background
Nice to have
• Velvetrope Logo on the bottom
Modern text that isn't curvy
Should not have
• Curved text

```html
<!DOCTYPE html>
<html lang="en">
<head>
<meta charset="utf-8">
<title>Lanternfall Nightclub – Velvetrope Atlanta</title>
<link href="https://fonts.googleapis.com/css2?family=Exo+2:wght@200;300;400&family=Josefin+Sans:wght@300;400&display=swap" rel="stylesheet">
<style>
  :root {
    --page-bg: #e7e7e7;
    --flyer-dark: #050505;
    --flyer-mid: #1c1c1c;
    --text-main: #f2f2f2;
    --text-soft: #d6d6d6;
    --rule: rgba(255, 255, 255, 0.55);
  }
  * { margin: 0; padding: 0; box-sizing: border-box; }
  html, body {
    width: 1200px;
    height: 1000px;
    overflow: hidden;
    background: var(--page-bg);
  }
  .flyer {
    position: absolute;
    left: 260px;
    top: 20px;
    width: 680px;
    height: 960px;
    background:
      radial-gradient(ellipse 60% 45% at 50% 45%, rgba(70, 70, 70, 0.55), rgba(0, 0, 0, 0) 70%),
      linear-gradient(180deg, var(--flyer-mid) 0%, var(--flyer-dark) 100%);
    color: var(--text-main);
    font-family: "Exo 2", sans-serif;
    text-align: center;
  }
  .flyer > * {
    position: absolute;
    left: 0;
    width: 100%;
  }
  .presenter {
    top: 36px;
    font-size: 26px;
    font-weight: 300;
    letter-spacing: 1px;
    text-transform: uppercase;
  }
  .club-mark {
    top: 130px;
    height: 110px;
    display: flex;
    justify-content: center;
  }
  .club-name {
    top: 318px;
    font-family: "Josefin Sans", sans-serif;
    font-size: 54px;
    font-weight: 300;
    letter-spacing: 8px;
    text-transform: uppercase;
    line-height: 1;
  }
  .club-type {
    top: 390px;
    font-family: "Josefin Sans", sans-serif;
    font-size: 27px;
    font-weight: 300;
    letter-spacing: 4px;
    text-transform: uppercase;
    line-height: 1;
  }
  .tagline {
    top: 497px;
    height: 96px;
    display: flex;
    flex-direction: column;
    justify-content: center;
    font-size: 23px;
    font-weight: 300;
    letter-spacing: 1px;
    line-height: 33px;
    text-transform: uppercase;
  }
  .tagline::before,
  .tagline::after {
    content: "";
    position: absolute;
    left: 97px;
    width: 486px;
    height: 1px;
    background: linear-gradient(90deg, transparent, var(--rule) 20%, var(--rule) 80%, transparent);
  }
  .tagline::before { top: 0; }
  .tagline::after { bottom: 0; }
  .event-time {
    top: 632px;
    font-size: 19px;
    font-weight: 300;
    line-height: 26px;
    color: var(--text-soft);
    text-transform: uppercase;
  }
  .access {
    top: 746px;
    font-size: 48px;
    font-weight: 200;
    letter-spacing: 3px;
    color: var(--text-soft);
    text-transform: uppercase;
  }
  .location-note {
    top: 856px;
    font-size: 18px;
    font-weight: 300;
    letter-spacing: 1px;
    text-transform: uppercase;
  }
  .host-name {
    top: 898px;
    display: flex;
    justify-content: center;
    align-items: center;
    gap: 10px;
    font-size: 15px;
    font-weight: 400;
    letter-spacing: 2px;
    text-transform: uppercase;
  }
  .host-name .dot {
    width: 12px;
    height: 12px;
    border: 1px solid var(--text-main);
  }
</style>
</head>
<body>
  <main class="flyer">
    <p class="presenter">Velvetrope Atlanta Presents</p>

    <div class="club-mark">
      <svg width="110" height="110" viewBox="0 0 110 110" aria-hidden="true">
        <circle cx="55" cy="55" r="48" fill="none" stroke="#e0e0e0" stroke-width="3"/>
      </svg>
    </div>

    <h1 class="club-name">Lanternfall</h1>
    <p class="club-type">Nightclub</p>

    <p class="tagline">
      <span>A Popup Nightclub Experience</span>
      <span>For One Night Only</span>
    </p>

    <p class="event-time">
      Friday, October 18, 2013<br>
      Party Begins at 9PM
    </p>

    <p class="access">Invite Only</p>

    <p class="location-note">See Invitation for Location Details</p>

    <p class="host-name"><span class="dot"></span>Velvetrope Atlanta</p>
  </main>
</body>
</html>
```